Cover for Piano Music Book

My wife is self publishing 15 piano pieces for beginners to intermediate pianists

Name of the book: Warm and Breezy. 15 short piano pieces for beginners to intermediate level.
Doriane Kelwick

The front cover is the main thing, but there needs to be something on the back. I will leave this to you, it could be plain or you could do something more imaginative.

A fun, colourful design is recommended to stand out. However it needs to appeal to both children and adults.
I need to have the psd of the design so we can change the wording if necessary. The book will be around A4 portrait size but the design needs to be flexible so the size of the cover can be changed if necessary.

```html
<!DOCTYPE html>
<html lang="en">
<head>
<meta charset="utf-8">
<title>Warm and Breezy — Book Cover</title>
<link rel="stylesheet" href="https://fonts.googleapis.com/css2?family=Great+Vibes&family=Open+Sans:wght@300;400;700&display=swap">
<style>
  :root {
    --page-bg: #ececec;
    --cover-black: #0b0807;
    --cover-deep: #1c1411;
    --title-white: #f7f5f2;
    --subtitle-grey: #b9b3ad;
    --author-grey: #a8a29c;
    --author-strong: #d6d0ca;
    --wood-dark: #2a140b;
    --wood-mid: #6a3519;
    --key-shadow: #2b2522;
    --key-grey: #8f8a84;
    --key-ivory: #cfc9c1;
    --key-soft: #aaa39a;
    --wood-base: #4e2716;
  }
  * { margin: 0; padding: 0; box-sizing: border-box; }
  html, body {
    width: 1100px; height: 1200px; overflow: hidden;
    background: var(--page-bg);
  }
  .cover {
    position: absolute; left: 220px; top: 60px;
    width: 660px; height: 1080px;
    background: linear-gradient(180deg, var(--cover-black) 0%, var(--cover-deep) 42%, var(--cover-black) 56%);
    overflow: hidden;
    font-family: "Open Sans", sans-serif;
  }
  .cover__title {
    position: absolute; left: 0; right: 0; top: 110px;
    text-align: center; color: var(--title-white);
    font-family: "Great Vibes", cursive; font-weight: 400; line-height: 1;
  }
  .cover__title-main { font-size: 124px; display: inline-block; }
  .cover__title-stack { display: inline-block; vertical-align: top; text-align: left; margin-left: 4px; }
  .cover__title-and { display: block; font-size: 44px; margin-top: 8px; }
  .cover__title-second { display: block; font-size: 66px; margin-top: 4px; }
  .cover__subtitle {
    position: absolute; left: 0; right: 0; top: 308px;
    text-align: center; color: var(--subtitle-grey);
    font-size: 12.5px; font-weight: 400; letter-spacing: 3.2px; text-transform: uppercase;
  }
  .cover__notes {
    position: absolute; left: 0; right: 0; top: 345px; height: 200px;
    background: radial-gradient(closest-side at 60% 50%, rgba(95,72,60,0.4), rgba(0,0,0,0));
  }
  .cover__author {
    position: absolute; left: 0; right: 0; top: 548px;
    text-align: center; font-size: 20px; letter-spacing: 3px; text-transform: uppercase;
    color: var(--author-grey); font-weight: 300;
  }
  .cover__author strong { font-weight: 700; color: var(--author-strong); }
  .cover__piano {
    position: absolute; left: 0; right: 0; top: 600px; bottom: 0;
    background:
      linear-gradient(100deg, rgba(0,0,0,0.35) 0%, rgba(0,0,0,0) 35%, rgba(0,0,0,0) 70%, rgba(0,0,0,0.25) 100%),
      linear-gradient(180deg, var(--wood-dark) 0%, var(--wood-mid) 7%, var(--key-shadow) 20%, var(--key-grey) 42%, var(--key-ivory) 66%, var(--key-soft) 88%, var(--wood-base) 100%);
  }
</style>
</head>
<body>
  <div class="cover">
    <h1 class="cover__title">
      <span class="cover__title-main">Warm</span><span class="cover__title-stack"><span class="cover__title-and">and</span><span class="cover__title-second">Breezy</span></span>
    </h1>
    <p class="cover__subtitle">15 short piano pieces for beginners to intermediate level</p>
    <div class="cover__notes" role="img" aria-label="Faint floating music notes over a dark background"></div>
    <p class="cover__author">Doriane <strong>Kelwick</strong></p>
    <div class="cover__piano" role="img" aria-label="Close-up photograph of black and ivory piano keys in perspective beneath a dark wooden fallboard"></div>
  </div>
</body>
</html>
```